Business card for Drone Aerial

I need a business card designed keeping in mind I want to do post cards also with a similar design.
Both sides of the card would be cool.
I have a skylark 5 max and would like a picture of it on the front of the card. Similar to one I attached.
I really like the look of a drone in the air and the background pic a little blurry. I attached a few images as IDEAS.
Some special things I want to be on the card additional to the normal business card info:
"Aerial Photography" or "Low Altitude Aerial Photography"?
"ZQB# 90817263"

I like modern and creative. My Favorite color is blue and I like blue on white.
I do not have a business name and am not going to have one. When they read "Aerial Photography" and see the drone and image they will know what the card is for.

FYI, The attached pictures are just images from framewillow and just samples/ideas.

Target Market(s)

Real estate, construction, events

Industry/Entity Type

Business

Contact Information for Business Card

Also Definitely want to contain, my name, my number and email address.

Requirements
Must have
• "ZQB# 90817263"
• "Aerial Photography"

```html
<!DOCTYPE html>
<html lang="en">
<head>
<meta charset="utf-8">
<title>Aerial Photography – Business Card</title>
<link rel="stylesheet" href="https://fonts.googleapis.com/css2?family=Orbitron:wght@500;700&family=Roboto:wght@500&family=Open+Sans:wght@400&display=swap">
<style>
  :root {
    --page-bg: #e8ebef;
    --ink: #1e1e1e;
    --sky-top: #f4f7fa;
    --sky-mid: #dfe9f2;
    --city-blue: #9fb6cc;
    --city-deep: #7f97ae;
    --band-dark: #1b1b1c;
    --band-panel: #232325;
    --band-edge: #8fa3b8;
    --accent-orange: #c8742a;
    --name-orange: #b9661f;
    --email-tone: #9a6533;
    --drone-white: #e9ecef;
    --drone-shade: #b7bec6;
  }
  html, body {
    margin: 0;
    width: 1200px;
    height: 900px;
    overflow: hidden;
    background: var(--page-bg);
  }
  .business-card {
    position: absolute;
    left: 150px;
    top: 193px;
    width: 900px;
    height: 514px;
    overflow: hidden;
    box-shadow: 0 14px 40px rgba(30, 40, 55, 0.22);
  }
  .card-backdrop {
    position: absolute;
    inset: 0;
    background: linear-gradient(180deg, var(--sky-top) 0%, var(--sky-mid) 38%, var(--city-blue) 68%, var(--city-deep) 100%);
  }
  .card-title {
    position: absolute;
    top: 38px;
    left: 0;
    width: 100%;
    margin: 0;
    text-align: center;
    font-family: "Orbitron", sans-serif;
    font-weight: 500;
    font-size: 33px;
    letter-spacing: 6px;
    color: var(--ink);
  }
  .licence-number {
    position: absolute;
    top: 88px;
    left: 0;
    width: 100%;
    text-align: center;
    font-family: "Roboto", sans-serif;
    font-weight: 500;
    font-size: 21px;
    letter-spacing: 1px;
    color: var(--ink);
  }
  .viewfinder {
    position: absolute;
    inset: 0;
  }
  .drone-photo {
    position: absolute;
    left: 266px;
    top: 130px;
    width: 384px;
    height: 214px;
    border-radius: 40% 40% 30% 30%;
    background: radial-gradient(ellipse at 50% 45%, var(--drone-white) 0%, var(--drone-shade) 55%, rgba(183, 190, 198, 0) 75%);
  }
  .contact-band {
    position: absolute;
    inset: 0;
  }
  .owner-name {
    position: absolute;
    left: 500px;
    top: 405px;
    width: 360px;
    text-align: center;
    font-family: "Orbitron", sans-serif;
    font-weight: 500;
    font-size: 23px;
    letter-spacing: 2px;
    color: var(--name-orange);
  }
  .contact-line {
    position: absolute;
    left: 46px;
    display: flex;
    align-items: center;
    gap: 10px;
    font-family: "Open Sans", sans-serif;
    font-size: 18px;
  }
  .contact-phone { top: 419px; color: var(--accent-orange); }
  .contact-email { top: 455px; color: var(--email-tone); }
</style>
</head>
<body>
  <div class="business-card">
    <div class="card-backdrop" role="img" aria-label="Softly blurred city skyline under a pale blue sky"></div>

    <h1 class="card-title">AERIAL PHOTOGRAPHY</h1>
    <div class="licence-number">ZQB# 90817263</div>

    <svg class="viewfinder" width="900" height="514" viewBox="0 0 900 514" aria-hidden="true">
      <g fill="none" stroke="#2a2a2a" stroke-width="2.5">
        <path d="M53,176 V134 H96"/>
        <path d="M804,134 H847 V176"/>
        <path d="M53,322 V364 H96"/>
        <path d="M804,364 H847 V322"/>
      </g>
    </svg>

    <div class="drone-photo" role="img" aria-label="White quadcopter drone with gimbal camera hovering in the air"></div>

    <svg class="contact-band" width="900" height="514" viewBox="0 0 900 514" aria-hidden="true">
      <path d="M0,400 L432,400 L462,455 L900,455 L900,514 L0,514 Z" fill="var(--band-dark)" opacity="0.92"/>
      <path d="M442,393 L900,393 L900,446 L472,446 Z" fill="var(--band-panel)"/>
      <path d="M442,393 L472,446" stroke="var(--band-edge)" stroke-width="3"/>
      <path d="M0,400 L433,400 L463,452 L900,452" fill="none" stroke="var(--accent-orange)" stroke-width="2.5"/>
    </svg>

    <div class="owner-name">MARCUS DELANEY</div>

    <div class="contact-line contact-phone">
      <svg width="16" height="16" viewBox="0 0 24 24" aria-hidden="true">
        <rect width="24" height="24" rx="3" fill="var(--accent-orange)"/>
        <path d="M7.5,5.5 l2.5,0 l1,3.5 l-1.6,1.2 c0.9,1.9 2.3,3.3 4.2,4.2 l1.2,-1.6 l3.5,1 l0,2.5 c0,0.8 -0.7,1.3 -1.4,1.3 C10.6,17.4 6.4,13.2 6.2,6.9 C6.2,6.2 6.7,5.5 7.5,5.5 Z" fill="#1b1b1c"/>
      </svg>
      <span>555-014-7730</span>
    </div>
    <div class="contact-line contact-email">
      <span>info@northgatecards.com</span>
    </div>
  </div>
</body>
</html>
```